Fashion Label Startup Business Card Design

Maribel Quint is a startup fashion designer based on the Gold Coast in QLD Australia. Maribels label " Vorine by Quint " is based upon taking old world design techniques and infusing them modern twist. The card design should incorporate an old world theme using colours like mustard, ocha, black, white and elements of lace pattern.

Card Details:

Maribel Quint
Fashion Designer
P: 04 0152 6847
E: vorinebyquint@mailbrook.com
W: www.friendsnet.com/VOrineByQuint

```html
<!DOCTYPE html>
<html lang="en">
<head>
<meta charset="utf-8">
<title>Vorine by Quint – Business Card</title>
<link rel="stylesheet" href="https://fonts.googleapis.com/css2?family=Pinyon+Script&family=Josefin+Sans:wght@400&display=swap">
<style>
  :root {
    --backdrop: #3b3330;
    --card-black: #121111;
    --ochre-tan: #d4a67a;
    --ochre-text: #dcae80;
    --ink: #141210;
  }
  * { margin: 0; padding: 0; box-sizing: border-box; }
  html, body {
    width: 1200px;
    height: 1000px;
    overflow: hidden;
    background: var(--backdrop);
  }
  .canvas {
    width: 1200px;
    height: 1000px;
    display: flex;
    flex-direction: column;
    align-items: center;
    justify-content: center;
    gap: 40px;
  }
  .card {
    width: 820px;
    height: 440px;
    background: var(--card-black);
    box-shadow: 0 10px 30px rgba(0,0,0,0.45);
    position: relative;
  }
  .card-front {
    display: flex;
    align-items: center;
    justify-content: center;
  }
  .label-name {
    font-family: "Pinyon Script", cursive;
    font-size: 78px;
    color: var(--ochre-text);
    letter-spacing: 2px;
    word-spacing: 14px;
    margin-top: -30px;
  }
  .card-back .panel {
    position: absolute;
    inset: 30px;
    background: var(--ochre-tan);
    color: var(--ink);
  }
  .designer {
    position: absolute;
    left: 0;
    right: 0;
    top: 150px;
    text-align: center;
  }
  .designer-name {
    font-family: "Pinyon Script", cursive;
    font-size: 64px;
    letter-spacing: 1px;
    word-spacing: 12px;
    line-height: 1;
  }
  .designer-role {
    font-family: "Josefin Sans", sans-serif;
    font-size: 17px;
    letter-spacing: 0.5px;
    margin-top: -4px;
    margin-left: -110px;
  }
  .contact {
    position: absolute;
    left: 30px;
    right: 30px;
    bottom: 22px;
    display: flex;
    justify-content: space-between;
    align-items: center;
    font-family: "Josefin Sans", sans-serif;
    font-size: 15px;
    letter-spacing: 0.6px;
  }
  .contact .sep {
    width: 7px;
    height: 7px;
    background: var(--ink);
    transform: rotate(45deg);
  }
</style>
</head>
<body>
  <main class="canvas">
    <section class="card card-front">
      <h1 class="label-name">Vorine by Quint</h1>
    </section>

    <section class="card card-back">
      <div class="panel">
        <div class="designer">
          <p class="designer-name">Maribel Quint</p>
          <p class="designer-role">Fashion Designer</p>
        </div>
        <div class="contact">
          <span class="phone">04 0152 6847</span>
          <span class="sep"></span>
          <span class="email">vorinebyquint@mailbrook.com</span>
          <span class="sep"></span>
          <span class="web">www.friendsnet.com/VOrineByQuint</span>
        </div>
      </div>
    </section>
  </main>
</body>
</html>
```